Extend Medium Rectangle into Halfpage and Billboard Ad Format

We have a few variations of our Medium Rectangle (300x250) that we use to build scalable online ads for local advertisers based on their images and logos which in most of the cases are very basic but still should deliver decent results in terms of overall banner look.

Based on those variations we would like to have each a Halfpage and Billboard variation to it that resembles the "look & feel" to feel like "out of one hand" and allows the local advertiser to recognize his ad across all formats.

Core of the Medium Rectangle is a carousel ad to swipe through the images and "more information" for the click-out to the landingpage. That might be great to replicate on the other banner formats but also could be done differently.

Attached the examples we have for one local customer to build ads from. Very limited but realistic.

```html
<!DOCTYPE html>
<html lang="de">
<head>
<meta charset="utf-8">
<title>Gasthof Falke – Halfpage &amp; Billboard</title>
<link href="https://fonts.googleapis.com/css2?family=Nunito+Sans:wght@700;800;900&display=swap" rel="stylesheet">
<style>
  :root {
    --red: #d0102a;
    --ink: #111111;
    --white: #ffffff;
    --dash: #e4e4e4;
    --page: #ffffff;
    --font: "Nunito Sans", Arial, sans-serif;
  }
  * { box-sizing: border-box; margin: 0; padding: 0; }
  html, body { width: 764px; height: 1200px; overflow: hidden; background: var(--page); }
  body { position: relative; font-family: var(--font); }

  .ad { position: absolute; overflow: hidden; background: var(--white);
        box-shadow: 1px 1px 2px rgba(0,0,0,.35), 0 0 1px rgba(0,0,0,.15); }
  .photo { position: absolute; inset: 0; }
  .photo--house { background: linear-gradient(180deg, #e4ebf2 0%, #d9dfe4 20%, #b2453a 32%, #ddd39a 45%, #d7cd95 62%, #8e8a72 78%, #6f6f4c 100%); }
  .photo--room  { background: linear-gradient(160deg, #efe4cc 0%, #cfae7d 30%, #a6442c 55%, #3d261c 80%, #6b4a2e 100%); }
  .photo--dish  { background: radial-gradient(ellipse at 55% 50%, #d59a55 0%, #b87a3c 30%, #6d3a22 55%, #d9cdc0 80%, #f4efe9 100%); }

  .cut { position: absolute; inset: 0; background: var(--white); }
  .halfpage .cut { clip-path: polygon(0 81.5%, 100% 51.7%, 100% 100%, 0 100%); }
  .billboard .cut { clip-path: polygon(61.3% 0, 100% 0, 100% 100%, 52.6% 100%); }

  .cta { position: absolute; height: 20px; padding: 0 15px 0 7px; background: var(--red);
         color: var(--white); font-weight: 800; font-size: 10.5px; line-height: 20px;
         clip-path: polygon(0 0, 100% 0, calc(100% - 6px) 100%, 0 100%); white-space: nowrap; }
  .billboard .cta { height: 22px; line-height: 22px; font-size: 12px; padding: 0 17px 0 7px; }

  .dots { position: absolute; display: flex; gap: 5px; }
  .dots span { width: 13px; height: 3px; background: var(--dash); }
  .billboard .dots span { width: 15px; gap: 5px; }
  .dots .is-active { background: var(--red); }

  .headline { position: absolute; font-weight: 900; color: var(--ink); line-height: 1.25; }
  .headline .accent { color: var(--red); }
  .halfpage .headline { left: 0; right: 0; text-align: center; font-size: 13.5px; }
  .billboard .headline { font-size: 16px; line-height: 1.3; }

  .brand { position: absolute; color: var(--red); font-weight: 700; letter-spacing: .5px; }
  .halfpage .brand { left: 0; right: 0; text-align: center; font-size: 20px; }
  .billboard .brand { font-size: 22px; left: 408px; }
</style>
</head>
<body>

  <!-- Halfpage set -->
  <section class="ad halfpage" style="left:69px; top:76px; width:192px; height:383px;">
    <div class="photo photo--house" role="img" aria-label="Foto: Gasthof-Fassade mit rotem Dach und Blumen im Vordergrund"></div>
    <div class="cut"></div>
    <a class="cta" style="left:51px; top:246px;">Mehr erfahren</a>
    <div class="dots" style="left:72px; top:277px;"><span class="is-active"></span><span></span><span></span></div>
    <h2 class="headline" style="top:291px;">Neueröffnung<br><span class="accent">Gasthof Falke</span><br>in Lindenau!</h2>
    <div class="brand" style="top:354px;">FALKE</div>
  </section>

  <section class="ad halfpage" style="left:279px; top:76px; width:192px; height:383px;">
    <div class="photo photo--room" role="img" aria-label="Foto: Gastraum mit gedeckten Tischen und roten Stühlen"></div>
    <div class="cut"></div>
    <a class="cta" style="left:51px; top:246px;">Mehr erfahren</a>
    <div class="dots" style="left:72px; top:277px;"><span></span><span class="is-active"></span><span></span></div>
    <div class="brand" style="top:327px;">FALKE</div>
  </section>

  <section class="ad halfpage" style="left:497px; top:76px; width:192px; height:383px;">
    <div class="photo photo--dish" role="img" aria-label="Foto: angerichtetes Gericht mit Kräutergarnitur"></div>
    <div class="cut"></div>
    <a class="cta" style="left:51px; top:246px;">Mehr erfahren</a>
    <div class="dots" style="left:72px; top:277px;"><span></span><span></span><span class="is-active"></span></div>
    <div class="brand" style="top:327px;">FALKE</div>
  </section>

  <!-- Billboard set -->
  <section class="ad billboard" style="left:128px; top:561px; width:511px; height:160px;">
    <div class="photo photo--house" role="img" aria-label="Foto: Gasthof-Fassade mit rotem Dach"></div>
    <div class="cut"></div>
    <a class="cta" style="left:242px; top:61px;">Mehr erfahren</a>
    <div class="dots" style="left:265px; top:96px;"><span class="is-active"></span><span></span><span></span></div>
    <div class="brand" style="top:22px;">FALKE</div>
    <h2 class="headline" style="left:374px; top:84px;">Neueröffnung<br><span class="accent">Gasthof Falke</span><br>in Lindenau!</h2>
  </section>

  <section class="ad billboard" style="left:128px; top:754px; width:511px; height:160px;">
    <div class="photo photo--room" role="img" aria-label="Foto: Gastraum mit gedeckten Tischen"></div>
    <div class="cut"></div>
    <a class="cta" style="left:242px; top:61px;">Mehr erfahren</a>
    <div class="dots" style="left:265px; top:96px;"><span></span><span class="is-active"></span><span></span></div>
    <div class="brand" style="top:22px;">FALKE</div>
  </section>

  <section class="ad billboard" style="left:128px; top:950px; width:511px; height:160px;">
    <div class="photo photo--dish" role="img" aria-label="Foto: angerichtetes Gericht in Nahaufnahme"></div>
    <div class="cut"></div>
    <a class="cta" style="left:242px; top:61px;">Mehr erfahren</a>
    <div class="dots" style="left:265px; top:96px;"><span></span><span></span><span class="is-active"></span></div>
    <div class="brand" style="top:22px;">FALKE</div>
  </section>

</body>
</html>
```